Stationery Design needed for logo design project

Our company needs a Stationery Design. Please refer to our original project in the link above.

Reason: Looking for more designs.

```html
<!DOCTYPE html>
<html lang="en">
<head>
<meta charset="utf-8">
<title>Korvan Stationery Set</title>
<link href="https://fonts.googleapis.com/css2?family=Montserrat:wght@600;800&family=Open+Sans:wght@400;600&family=Dancing+Script:wght@700&display=swap" rel="stylesheet">
<style>
  :root {
    --red: #c41f26;
    --red-bright: #d9252c;
    --black: #141414;
    --ink: #1c1c1c;
    --grey-text: #6a6a6a;
    --paper: #f7f7f7;
    --stage: #e6e6e8;
  }
  * { box-sizing: border-box; margin: 0; padding: 0; }
  html, body { width: 1200px; height: 905px; overflow: hidden; background: var(--stage); }
  .canvas { position: relative; width: 1200px; height: 905px; font-family: "Open Sans", sans-serif; color: var(--ink); }
  .sheet { position: absolute; background: var(--paper); overflow: hidden; box-shadow: 0 1px 3px rgba(0,0,0,.12); }

  /* brand name lockup */
  .brand { display: flex; align-items: center; gap: 6px; font-family: "Montserrat", sans-serif; font-weight: 800; color: var(--ink); letter-spacing: .04em; line-height: 1; }
  .brand-square { display: block; background: var(--red); }
  .brand--light { color: #fff; }
  .brand--light .brand-square { background: #fff; }

  /* two-tone footer stripe */
  .stripe { position: absolute; left: 0; right: 0; bottom: 0; display: flex; }
  .stripe-red { flex: 0 0 62%; background: var(--red); }
  .stripe-black { flex: 1; background: var(--black); }

  /* letterhead */
  .letterhead { left: 30px; top: 30px; width: 380px; height: 537px; }
  .letterhead .brand { position: absolute; left: 30px; top: 34px; font-size: 17px; }
  .letterhead .brand-square { width: 14px; height: 14px; }
  .letter-body { position: absolute; left: 30px; right: 34px; top: 96px; font-size: 6.6px; line-height: 1.6; color: #333; }
  .letter-body p { margin-bottom: 9px; }
  .signature { display: block; width: 70px; height: 20px; margin: 4px 0 4px; background: linear-gradient(90deg, #d5d5d5, #ececec); border-radius: 3px; }
  .signer { font-size: 6.6px; font-weight: 600; }
  .letter-contact { position: absolute; left: 30px; bottom: 16px; font-size: 6px; line-height: 1.7; color: #444; }
  .letter-contact .dot, .card-contact .dot, .slip-contact .dot { display: inline-block; width: 5px; height: 5px; background: var(--red); border-radius: 50%; margin-right: 4px; vertical-align: middle; }
  .letterhead .stripe { height: 6px; }

  /* presentation folder */
  .folder { left: 430px; top: 30px; width: 380px; height: 537px; }
  .folder .brand { position: absolute; left: 130px; top: 90px; font-size: 20px; }
  .folder .brand-square { width: 16px; height: 16px; }
  .folder-band { position: absolute; left: 0; right: 0; top: 228px; height: 7px; background: var(--black); }
  .folder-panel { position: absolute; left: 0; right: 0; top: 235px; bottom: 0; background: var(--red); }
  .folder-edge { position: absolute; left: 0; top: 0; bottom: 0; width: 5px; background: var(--black); }

  /* envelopes */
  .envelope-front { left: 830px; top: 30px; width: 340px; height: 170px; }
  .envelope-front .brand { position: absolute; left: 24px; top: 70px; font-size: 13px; }
  .envelope-front .brand-square { width: 11px; height: 11px; }
  .envelope-address { position: absolute; left: 24px; top: 92px; font-size: 5.6px; color: #555; }
  .envelope-front .stripe { height: 6px; }
  .envelope-edge { position: absolute; right: 0; top: 0; width: 40%; height: 6px; background: var(--black); }
  .envelope-back { left: 830px; top: 218px; width: 340px; height: 170px; }
  .envelope-flap { position: absolute; left: 0; right: 0; top: 0; height: 96px; background: var(--red); border-radius: 0 0 70px 70px / 0 0 22px 22px; }
  .flap-mark { position: absolute; left: 162px; top: 40px; width: 16px; height: 16px; background: #fff; }

  /* business cards */
  .card-front { left: 870px; top: 408px; width: 260px; height: 148px; }
  .card-front .brand { position: absolute; left: 18px; top: 20px; font-size: 14px; }
  .card-front .brand-square { width: 11px; height: 11px; }
  .card-name { position: absolute; left: 18px; top: 48px; font-family: "Montserrat", sans-serif; font-weight: 600; font-size: 8px; }
  .card-title { display: block; font-family: "Open Sans", sans-serif; font-weight: 400; font-size: 6px; color: var(--grey-text); margin-top: 2px; }
  .card-contact { position: absolute; left: 18px; top: 80px; font-size: 6px; line-height: 1.75; color: #444; }
  .card-front .stripe { height: 6px; }
  .card-back { left: 870px; top: 660px; width: 260px; height: 148px; background: var(--red-bright); }
  .card-back .brand { position: absolute; left: 78px; top: 66px; font-size: 17px; }
  .card-back .brand-square { width: 13px; height: 13px; }

  /* notebook */
  .notebook { left: 30px; top: 600px; width: 195px; height: 275px; }
  .notebook-spiral { position: absolute; left: 0; top: 0; bottom: 0; width: 10px; background: repeating-linear-gradient(180deg, #555 0 3px, transparent 3px 8px); }
  .notebook .brand { position: absolute; left: 42px; top: 34px; font-size: 13px; }
  .notebook .brand-square { width: 10px; height: 10px; }
  .notebook-band { position: absolute; left: 10px; right: 0; top: 104px; height: 5px; background: var(--black); }
  .notebook-panel { position: absolute; left: 10px; right: 0; top: 109px; bottom: 0; background: var(--red); }

  /* compliment slip */
  .slip { left: 250px; top: 600px; width: 580px; height: 275px; }
  .slip .brand { position: absolute; left: 36px; top: 150px; font-size: 18px; }
  .slip .brand-square { width: 14px; height: 14px; }
  .slip-heading { position: absolute; right: 44px; top: 98px; font-family: "Dancing Script", cursive; font-weight: 700; font-size: 30px; color: var(--red); }
  .slip-contact { position: absolute; left: 36px; bottom: 22px; font-size: 7px; line-height: 1.7; color: #444; }
  .slip-edge { position: absolute; right: 0; top: 0; bottom: 0; width: 16px; background: var(--black); }
  .slip .stripe { height: 7px; right: 16px; }
  .slip .stripe-red { flex-basis: 40%; }
  .slip .stripe-black { background: transparent; }
</style>
</head>
<body>
<main class="canvas">

  <section class="sheet letterhead" aria-label="Letterhead">
    <div class="brand"><span class="brand-square"></span>KORVAN</div>
    <div class="letter-body">
      <p>Dear Client,</p>
      <p>Thank you for choosing our laboratory team. We are pleased to confirm that your samples arrived safely and testing has begun this week. Our analysts will share a full report with clear results and notes as soon as each stage is complete.</p>
      <p>Our services cover sample handling, calibration, quality checks and detailed reporting for clients across many sectors. Each project is reviewed by a senior scientist before release, so you can rely on accurate data delivered on time and explained in plain language.</p>
      <p>Please contact our office if you have any questions about timelines or pricing. We look forward to working with you again.</p>
      <p>Kind regards,</p>
      <span class="signature" role="img" aria-label="Handwritten signature"></span>
      <div class="signer">Daniel Reyes, Managing Director</div>
    </div>
    <div class="letter-contact">
      <div><span class="dot"></span>210 Harbor Road, Suite 4, Dayton, OH 45402</div>
      <div><span class="dot"></span>+1 555 014 2280 &nbsp; <span class="dot"></span>hello@korvanlabs.com &nbsp; <span class="dot"></span>www.korvanlabs.com</div>
    </div>
    <div class="stripe"><span class="stripe-red"></span><span class="stripe-black"></span></div>
  </section>

  <section class="sheet folder" aria-label="Presentation folder">
    <div class="folder-edge"></div>
    <div class="brand"><span class="brand-square"></span>KORVAN</div>
    <div class="folder-band"></div>
    <div class="folder-panel"></div>
  </section>

  <section class="sheet envelope-front" aria-label="Envelope front">
    <div class="envelope-edge"></div>
    <div class="brand"><span class="brand-square"></span>KORVAN</div>
    <div class="envelope-address">210 Harbor Road, Suite 4, Dayton, OH 45402</div>
    <div class="stripe"><span class="stripe-red"></span><span class="stripe-black"></span></div>
  </section>

  <section class="sheet envelope-back" aria-label="Envelope back">
    <div class="envelope-flap"><span class="flap-mark"></span></div>
  </section>

  <section class="sheet card-front" aria-label="Business card front">
    <div class="brand"><span class="brand-square"></span>KORVAN</div>
    <div class="card-name">Daniel Reyes<span class="card-title">Managing Director</span></div>
    <div class="card-contact">
      <div><span class="dot"></span>+1 555 014 2280</div>
      <div><span class="dot"></span>hello@korvanlabs.com</div>
      <div><span class="dot"></span>www.korvanlabs.com</div>
    </div>
    <div class="stripe"><span class="stripe-red"></span><span class="stripe-black"></span></div>
  </section>

  <section class="sheet card-back" aria-label="Business card back">
    <div class="brand brand--light"><span class="brand-square"></span>KORVAN</div>
  </section>

  <section class="sheet notebook" aria-label="Notebook cover">
    <div class="notebook-spiral"></div>
    <div class="brand"><span class="brand-square"></span>KORVAN</div>
    <div class="notebook-band"></div>
    <div class="notebook-panel"></div>
  </section>

  <section class="sheet slip" aria-label="Compliment slip">
    <div class="slip-heading">With Compliments</div>
    <div class="brand"><span class="brand-square"></span>KORVAN</div>
    <div class="slip-contact">
      <div><span class="dot"></span>210 Harbor Road, Suite 4, Dayton, OH 45402</div>
      <div><span class="dot"></span>+1 555 014 2280 &nbsp; <span class="dot"></span>hello@korvanlabs.com &nbsp; <span class="dot"></span>www.korvanlabs.com</div>
    </div>
    <div class="slip-edge"></div>
    <div class="stripe"><span class="stripe-red"></span><span class="stripe-black"></span></div>
  </section>

</main>
</body>
</html>
```